Plakat-Design für LACH-TRANCE-ABEND
Zielgruppe
Ich bin Hypnotiseur und trete europaweit bei div. Events mit meiner LACH-TRANCE-ABEND auf (www.lach-trance-abend.example)
Aufgabenstellung
Das Plakat sollte die Elemente Hypnose+Comedy darstellen. Es wird für ein renommiertes Theater gebraucht für deren Leuchtkästen im Format: TIFF/PSD (alternativ JPG) 594mm x 840mm + 1mm Beschnitt.
Das Plakat sollte unten ein freies Störerfeld haben, damit dieses auch für zukünftige Gastspiele genutzt werden kann.
INFOS auf dem Plakat:
-Künstlername (=Varomir)
-Lach-Trance-Abend
-echte Live-Hypnose
Die Show heisst "Träum!" (wie auf einigen Bildern von mir ja dargestellt)
Das Plakat sollte eine gewisse Wertigkeit vermitteln, etwas exklusives, einmaliges. Die Show ist für Erwachsene, daher kein kindliches, zu verspieltes Design. Lieber klar und exklusiv, hochwertig. Danke!

```html
<!DOCTYPE html>
<html lang="de">
<head>
<meta charset="utf-8">
<title>Träum! – Lach-Trance-Abend Plakat</title>
<link rel="stylesheet" href="https://fonts.googleapis.com/css2?family=Cinzel:wght@400;500&family=Cinzel+Decorative:wght@400&display=swap">
<style>
  :root {
    --stage: #1a1c24;
    --poster-black: #07060a;
    --nebula-violet: #6a3a9a;
    --nebula-pink: #b86aa8;
    --deep-space: #1b1436;
    --text-light: #e6e0ea;
    --text-muted: #c9c2cc;
    --gold: #d8b24a;
    --title-pink: #f1c6e0;
    --title-rose: #c9829f;
    --title-gold: #e3b56a;
  }
  * { margin: 0; padding: 0; box-sizing: border-box; }
  html, body { width: 1200px; height: 797px; overflow: hidden; }
  body { background: var(--stage); position: relative; }

  .poster {
    position: absolute;
    left: 347px; top: 18px;
    width: 505px; height: 760px;
    background: var(--poster-black);
    overflow: hidden;
    font-family: "Cinzel", serif;
    color: var(--text-light);
  }
  .poster__visual {
    position: absolute; inset: 0 0 auto 0;
    height: 640px;
    background:
      radial-gradient(ellipse 38% 36% at 50% 36%, rgba(205,150,160,0.55), transparent 70%),
      radial-gradient(ellipse 40% 30% at 12% 45%, rgba(150,70,170,0.55), transparent 70%),
      radial-gradient(ellipse 35% 25% at 88% 52%, rgba(184,106,168,0.45), transparent 70%),
      linear-gradient(180deg, var(--deep-space) 0%, #2a1d4a 45%, #120d1e 75%, var(--poster-black) 100%);
  }
  .poster__artist {
    position: absolute; left: 97px; top: 452px;
    font-size: 27px; letter-spacing: 1px; font-weight: 400;
    color: var(--text-light);
  }
  .poster__title {
    position: absolute; left: 0; right: 0; top: 480px;
    text-align: center;
    font-family: "Cinzel Decorative", serif;
    font-size: 84px; line-height: 1; letter-spacing: 1px;
    background: linear-gradient(90deg, var(--title-pink) 0%, var(--title-rose) 35%, var(--title-gold) 55%, var(--title-rose) 80%, var(--title-pink) 100%);
    -webkit-background-clip: text; background-clip: text;
    color: transparent;
  }
  .poster__tagline {
    position: absolute; left: 0; right: 0; top: 606px;
    text-align: center;
    font-size: 13px; letter-spacing: 1.6px;
    word-spacing: 2px;
  }
  .poster__tagline .gap { display: inline-block; width: 18px; }
  .poster__copy {
    position: absolute; left: 0; right: 0; top: 634px;
    text-align: center;
    font-size: 6.5px; line-height: 11px; letter-spacing: 0.4px;
    color: var(--text-muted); text-transform: uppercase;
  }
  .poster__brand {
    position: absolute; left: 0; right: 0; top: 684px;
    text-align: center;
    font-size: 9px; letter-spacing: 1px;
    color: var(--text-light);
  }
  .poster__url {
    position: absolute; left: 0; right: 0; top: 719px;
    text-align: center;
    font-size: 10px; letter-spacing: 1.2px;
    color: var(--gold); text-transform: uppercase;
  }
  .poster__rule {
    position: absolute; left: 10px; right: 10px; top: 736px;
    height: 1px; background: rgba(216,178,74,0.35);
  }
  .poster__footer {
    position: absolute; left: 0; right: 0; top: 744px;
    text-align: center;
    font-size: 6px; letter-spacing: 1px;
    color: var(--text-muted); text-transform: uppercase;
  }
</style>
</head>
<body>
  <main class="poster">
    <div class="poster__visual" role="img" aria-label="Porträt des Hypnotiseurs vor einem violetten Sternennebel"></div>

    <p class="poster__artist">VAROMIR</p>
    <h1 class="poster__title">TRÄUM!</h1>
    <p class="poster__tagline">LACH-TRANCE-ABEND<span class="gap"></span>- ECHTE LIVE-HYPNOSE</p>

    <p class="poster__copy">
      Eine einzigartige Show, die Ihre Gäste garantiert nicht vergessen werden!<br>
      So etwas haben Sie sicherlich noch nicht gesehen und erlebt!<br>
      Bestes, witziges und unvergessliches Entertainment
    </p>

    <p class="poster__brand">Varomir</p>
    <p class="poster__url">www.lach-trance-abend.example</p>
    <div class="poster__rule"></div>
    <p class="poster__footer">Show info and ticket booking info goes here - show info and ticket booking info goes here</p>
  </main>
</body>
</html>
```